Stalwart Noble Alloys Foundries Business Cards

Business Card Design Description
We are wanting to have a new business card designed for our company as we go to a convention. We want to balance business/Modern with elegance and beauty. Our company sells highend jewelry pieces. We want to utilize the colors of Black and Gold and have gold foiled fonts to be physically printed on the business cards.
We also would like to have space to write notes on the back side of the business card. When we meet people at jewelry conventions we would like to write notes if possible.
Here are websites and designs that we like the look and feel of these companies and you can use these as design ideas.
https://www.bellwynne.com
https://www.morvandel.com/en-us/home
Here is our company website link
www.stalwartnaf.com
I also up loaded two versions of our logo.
- Update 4.26.22
I have uploaded photos of a business card we like. this card has raised embossed letters that you can feel. the raise letters are like a plastic but we don't need to use that...I uploaded to show you that we like the experience of the client feeling the characters of the logo. we also would like to have the material as a satin or some material very soft.
- Maybe we can get designs with beautiful gold foiling and raised characters and logos. we like simplicity...not busy but an elegant design. We need to write notes and would like a section where we can write notes. but we want an elegant style and the client has an experience with the feel of the card when they touch the card.
Colors
- Main colors Black & Gold
- white or light colors for small notes section.
Specialty ideals and things we would like to see based on your design styles.
- raised fonts
- raised logos
- gold foiling
- satin/soft finish on the card material.
we are wanting to design a business card that looks elegant and clean. When the client is handed the business card we want them to physically experience the business card as well by touching the raised logos or fonts and the base material is soft satin. I hope this helps with further designs.
thank you all
We uploaded a new contact layout that we have designed in our office. we would like to see how this would look on your designs.
thank you
I just finished uploading the Contact Layout. the colors are just examples. please use this layout as an idea and use colors based on the feed back we have given each of you personally.
Contact Information for Business Card
we need an area to write notes, we would like to have our logos or the diamond of our logo or the business card to have embossed sections to the business card so when the customer touches the card they can feel the logo. we would also like sections of our business card to have gold foiling. we would also like to use a satin soft paper with our card. when the client touches the card its super soft and high quality
Requirements
Must have
- we would like to have our logos or the diamond of our logo or the business card to have embossed sections to the business card so when the customer touches the card they can feel the logo. we would also like sections of our business card to have gold foiling. we would also like to use a satin soft paper with our card. when the client touches the card its super soft and high quality
Nice to have
- we would like to have our logos or the diamond of our logo or the business card to have embossed sections to the business card so when the customer touches the card they can feel the logo. we would also like sections of our business card to have gold foiling.

```html
<!DOCTYPE html>
<html lang="en">
<head>
<meta charset="utf-8">
<title>Halvorsen Rowe – Business Cards</title>
<link rel="stylesheet" href="https://fonts.googleapis.com/css2?family=Arimo:wght@700&display=swap">
<style>
  :root {
    --backdrop: #c2c2c2;
    --gold: #c9a048;
    --gold-deep: #a67f2c;
    --gold-light: #e2c27a;
    --ink: #1c1c1c;
    --paper: #ffffff;
  }
  * { box-sizing: border-box; margin: 0; padding: 0; }
  html, body {
    width: 1200px; height: 957px; overflow: hidden;
    background: var(--backdrop);
  }
  .stage { position: relative; width: 1200px; height: 957px; }

  .card {
    position: absolute;
    width: 540px; height: 320px;
    box-shadow: 0 14px 30px rgba(0,0,0,0.22);
  }

  /* Front: white contact side */
  .card--front {
    left: 60px; top: 470px;
    background: var(--paper);
    overflow: hidden;
  }
  .card--front .band {
    position: absolute; right: 0; width: 290px; height: 16px;
    background: var(--gold);
  }
  .card--front .band--top { top: 0; }
  .card--front .band--bottom { bottom: 0; }

  .card--front .brand {
    position: absolute; left: 20px; top: 0; bottom: 0; width: 220px;
    display: flex; align-items: center; justify-content: center;
    text-align: center;
    font-family: "Arimo", sans-serif; font-weight: 700;
    font-size: 22px; line-height: 1.2;
    color: var(--gold);
  }

  .contact {
    position: absolute; left: 270px; top: 58px; width: 240px;
    font-family: "Arimo", sans-serif; font-weight: 700;
    color: var(--gold);
  }
  .contact .person-name { font-size: 24px; line-height: 1; }
  .contact .person-title { font-size: 12px; margin-top: 4px; }
  .contact .rule {
    height: 2px; background: var(--gold);
    margin: 10px 0 10px; width: 230px;
  }
  .contact ul { list-style: none; }
  .contact li {
    display: flex; align-items: center; gap: 9px;
    font-size: 16px; line-height: 24px;
  }
  .contact li svg { width: 13px; height: 13px; flex: none; }

  /* Back: black foil-framed side */
  .card--back {
    left: 600px; top: 120px;
    background: var(--ink);
    border: 9px solid var(--gold-deep);
    outline: 2px solid var(--gold-light);
    outline-offset: -11px;
    display: flex; align-items: center; justify-content: center;
  }
  .card--back .brand {
    font-family: "Arimo", sans-serif; font-weight: 700;
    font-size: 32px; line-height: 1.2;
    color: var(--gold);
    text-align: center;
  }
</style>
</head>
<body>
<main class="stage">

  <section class="card card--back" aria-label="Business card, back">
    <p class="brand">Halvorsen Rowe</p>
  </section>

  <section class="card card--front" aria-label="Business card, front">
    <div class="band band--top"></div>
    <div class="band band--bottom"></div>

    <p class="brand">Halvorsen Rowe</p>

    <div class="contact">
      <p class="person-name">Name Here</p>
      <p class="person-title">Title Here</p>
      <div class="rule"></div>
      <ul>
        <li>
          <svg viewBox="0 0 12 12" aria-hidden="true"><rect x="3" y="0.5" width="6" height="11" rx="1" fill="none" stroke="currentColor" stroke-width="1.4"/><circle cx="6" cy="9.3" r="0.8" fill="currentColor"/></svg>
          000 000 0000
        </li>
        <li>
          <svg viewBox="0 0 12 12" aria-hidden="true"><path d="M1 5 Q6 1 11 5 L10 7 L8 6 L8 5 Q6 4 4 5 L4 6 L2 7 Z" fill="currentColor"/><rect x="3" y="7" width="6" height="4" rx="1" fill="currentColor"/></svg>
          000 000 0000
        </li>
        <li>
          <svg viewBox="0 0 12 12" aria-hidden="true"><rect x="1" y="4" width="10" height="7" rx="1" fill="none" stroke="currentColor" stroke-width="1.4"/><rect x="3" y="1" width="6" height="4" fill="none" stroke="currentColor" stroke-width="1.2"/></svg>
          000 000 0000
        </li>
        <li>
          <svg viewBox="0 0 12 12" aria-hidden="true"><rect x="1" y="2.5" width="10" height="7" rx="1" fill="none" stroke="currentColor" stroke-width="1.4"/><path d="M1.5 3 L6 7 L10.5 3" fill="none" stroke="currentColor" stroke-width="1.2"/></svg>
          info@domain.com
        </li>
        <li>
          <svg viewBox="0 0 12 12" aria-hidden="true"><circle cx="7" cy="5" r="3.5" fill="none" stroke="currentColor" stroke-width="1.4"/><path d="M4.5 7.5 L1 11" stroke="currentColor" stroke-width="1.6"/></svg>
          www.domain.com
        </li>
      </ul>
    </div>
  </section>

</main>
</body>
</html>
```